Brightwave Partners, Inc. Website redesign

Revamp the website, it is old and outdated. www.brightwavepartnersinc.example

Target Market(s)

Information Technology Consulting and Staffing

Coding

Coded - Design and coding required

Number of Pages Required

5+ page

Colors

Designer to choose colors to be used in the design.

Requirements
Must have
• Outlined text boxes just like from the Tolvane.us site. A clean look

```html
<!DOCTYPE html>
<html lang="en">
<head>
<meta charset="utf-8">
<title>Brightwave Partners, Inc.</title>
<link rel="stylesheet" href="https://fonts.googleapis.com/css2?family=Orbitron:wght@600;700&family=Open+Sans:wght@400;700&family=Roboto+Condensed:wght@400;700&family=Cinzel:wght@400&family=Arimo:wght@700&display=swap">
<style>
  :root {
    --frame: #e6e6e6;
    --white: #ffffff;
    --muted: #333333;
    --blue: #0a33a0;
    --band: #1c1a19;
    --red: #9b1b2e;
    --maroon: #4b0e19;
    --pink: #c98690;
    --footer: #222222;
  }
  * { box-sizing: border-box; margin: 0; padding: 0; }
  html, body { width: 877px; height: 1200px; overflow: hidden; }
  body { background: var(--frame); position: relative; font-family: "Open Sans", sans-serif; }
  .page { position: absolute; left: 9px; top: 9px; width: 859px; height: 1182px; background: var(--white); overflow: hidden; }

  .hero { position: absolute; left: 0; top: 0; width: 859px; height: 470px; }
  .hero-photo { position: absolute; inset: 0;
    background:
      radial-gradient(ellipse at 60% 45%, rgba(60,150,160,.35), transparent 55%),
      radial-gradient(ellipse at 20% 60%, rgba(110,120,130,.45), transparent 40%),
      linear-gradient(90deg, #151c26 0%, #27313d 30%, #0d1620 55%, #3a4652 100%); }
  .brand { position: absolute; left: 22px; top: 29px; display: flex; align-items: center; gap: 14px; color: var(--white); white-space: nowrap; }
  .brand-name { font-family: "Open Sans", sans-serif; font-weight: 700; font-size: 15px; letter-spacing: .3px; }
  .tagline { font-family: "Cinzel", serif; font-size: 15px; color: #e8eef2; }
  .menu { position: absolute; left: 805px; top: 37px; width: 30px; height: 26px; }
  .menu span { display: block; height: 5px; border-radius: 3px; background: var(--white); margin-bottom: 5.5px; }
  .headline { position: absolute; left: 0; right: 0; top: 192px; text-align: center; font-family: "Orbitron", sans-serif; font-weight: 700; font-size: 33px; line-height: 36px; color: #f2f4f6; text-shadow: 0 2px 4px rgba(0,0,0,.7); white-space: nowrap; }

  .intro { position: absolute; left: 42px; top: 513px; width: 775px; text-align: center; font-family: "Roboto Condensed", sans-serif; font-size: 13px; line-height: 15.8px; color: var(--muted); }
  .cta { position: absolute; left: 351px; top: 611px; width: 157px; height: 31px; border-radius: 16px; background: var(--blue); color: var(--white); font-family: "Roboto Condensed", sans-serif; font-weight: 700; font-size: 12.5px; line-height: 31px; text-align: center; box-shadow: 0 4px 10px rgba(40,110,255,.45); }

  .band { position: absolute; left: 0; top: 680px; width: 859px; height: 279px; background: radial-gradient(ellipse at 50% 0%, #3a3634, var(--band) 70%); }

  .cards { position: absolute; left: 66px; top: 730px; display: flex; gap: 25px; }
  .card { position: relative; width: 226px; height: 379px; background: var(--white); box-shadow: 0 2px 8px rgba(0,0,0,.15); }
  .card::before { content: ""; position: absolute; left: 16px; top: 0; width: 63px; height: 4px; background: var(--red); }
  .card-title { position: absolute; left: 17px; top: 16px; font-weight: 700; font-size: 14px; color: #111; }
  .card-title em { font-style: normal; color: var(--red); }
  .card-image { position: absolute; left: 0; top: 41px; width: 226px; height: 138px; }
  .img-about { background: linear-gradient(120deg, #dfe6ea, #9fb3bf 45%, #eef1f2 80%); }
  .img-services { background: radial-gradient(ellipse at 55% 45%, #4fb2ff, #0b4fa8 50%, #0a2347 100%); }
  .img-strategy { background: radial-gradient(ellipse at 45% 50%, #1f7de8, #0b2f7a 55%, #0a1326 100%); }
  .card-text { position: absolute; left: 17px; top: 189px; width: 206px; font-size: 10.2px; line-height: 15.2px; color: #222; }
  .read-more { position: absolute; left: 22px; top: 321px; width: 144px; height: 31px; background: var(--maroon); color: var(--white); font-weight: 700; font-size: 12.5px; line-height: 31px; padding-left: 11px; box-shadow: -6px -6px 0 #000, 6px 6px 0 var(--pink); }
  .read-more svg { position: absolute; right: 14px; top: 9px; }

  .footer { position: absolute; left: 0; top: 1153px; width: 859px; height: 29px; background: var(--footer); color: var(--white); font-family: "Arimo", sans-serif; font-weight: 700; font-size: 8.5px; line-height: 29px; text-align: center; }
</style>
</head>
<body>
<div class="page">
  <header class="hero">
    <div class="hero-photo" role="img" aria-label="Businessman in a dark suit touching a glowing network of teal connected nodes"></div>
    <div class="brand">
      <span class="brand-name">Brightwave Partners</span>
      <span class="tagline">Mission Integrity Results</span>
    </div>
    <div class="menu" aria-label="Menu"><span></span><span></span><span></span></div>
    <h1 class="headline">Bringing Thought Leadership and<br>Quality to Every Project</h1>
  </header>

  <p class="intro">Brightwave Partners, Inc. is an 8(a) full-service IT consulting company based in the Washington, DC Metro area. We offer specialized, highly customized technology solutions for our customers located throughout the United States. No two businesses are the same. We believe the technology supporting your business operations should align with your company. Every project begins with a thorough analysis of your current technology environment. We work with you to define the environment you want. Then we implement industry-proven practices that enable you to achieve your business objectives. We draw on our experience at civilian and federal agencies to generate ideas and create IT solutions that address your unique business needs.</p>
  <a class="cta">GET STARTED</a>

  <div class="band"></div>

  <section class="cards">
    <article class="card">
      <h2 class="card-title">ABOUT <em>US</em></h2>
      <div class="card-image img-about" role="img" aria-label="Colleagues gesturing over a laptop with digital overlays"></div>
      <p class="card-text">Brightwave Partners, Inc. is an 8(a) innovative and rapidly growing full-service IT consulting firm. We provide our clients with cutting-edge technologies and the know-how to apply them to their individual business models.</p>
      <a class="read-more">Read More<svg width="13" height="13" viewBox="0 0 13 13"><path d="M1 6.5h10M6.5 2l4.5 4.5L6.5 11" fill="none" stroke="#fff" stroke-width="1.6"/></svg></a>
    </article>
    <article class="card">
      <h2 class="card-title">SERVICES</h2>
      <div class="card-image img-services" role="img" aria-label="Hand using a tablet with glowing blue technology icons"></div>
      <p class="card-text">Brightwave Partners, Inc. organizes our Services into four key areas. While these four services can be implemented individually the majority of our projects successfuly combine componets from each. Our people and our process is what makes us successful in providing these services.</p>
      <a class="read-more">Read More<svg width="13" height="13" viewBox="0 0 13 13"><path d="M1 6.5h10M6.5 2l4.5 4.5L6.5 11" fill="none" stroke="#fff" stroke-width="1.6"/></svg></a>
    </article>
    <article class="card">
      <h2 class="card-title">STRATEGY</h2>
      <div class="card-image img-strategy" role="img" aria-label="Hand placing a glowing blue gear among interlocking gears"></div>
      <p class="card-text">Savvy businesses understand that technology investments cannot be made solely to enable internal and external operations; technology is now, more than ever, a critical component to retaining and winning customers as well as staying ahead of the competition.</p>
      <a class="read-more">Read More<svg width="13" height="13" viewBox="0 0 13 13"><path d="M1 6.5h10M6.5 2l4.5 4.5L6.5 11" fill="none" stroke="#fff" stroke-width="1.6"/></svg></a>
    </article>
  </section>

  <footer class="footer">COPYRIGHT © 2019 BRIGHTWAVE PARTNERS. ALL RIGHTS RESERVED.</footer>
</div>
</body>
</html>
```